Need help refining Tallbergsgillet

Hi We need help with the refining of overall design and details of our homepage design Tallbergsgillet. See attached files.

Attached files:
homepage.psd - file you can use to work from.
homepage.png – quick notes on thoughts of the design
logo.psd (smart object) – The logo should be in gold.
social media elements.png - what type of data that needs design in the feed

What we need:
Something is missing with the overall design as well as detailed design for our social media feed. We don’t know what and hope you can solve this for us.

The homepage:
Our main page include a selfloading blogfeed combined with Vendraly- and Instagramfeed.

Fonts:
So far I´ve used Roboto regular, and Georgia, but feel free to use other fonts if you find better suited

Among others, we need a better detailed design that works better with the overall design.

Se attached sample image (social_mediafeed.png) what types of data we get from Vendraly in our feed. Feel free to redesign the elements of this data.

Headerlinks:
Even though we only have one page, there should be place for links to other pages as well which will load below the header.

Social media follow: Place for social media follow links/icons/buttons in style with rest of the design. Maybe at top grey border? We use Glimtora and Vendraly in style with rest of the design.

Colors:
The logo should be in gold, and use of "goldish" colors troughout the page.
Also blue elements troughout the page

Logo in gold/goldish color
Blue elements # 13416c (or similar color that works well in the design)

Target Market(s)

Wellness, fitness, spa and food, Exclusive

Number of Pages Required

1 page

Font styles to use
Serif
Sans Serif
Script
Other font styles liked:
• Roboto, Georgia

Requirements
Must have
• Better overall design that feel harmonic.
• Better design of blog and social media feeds (se all attached images)
• Nice clean design, easy on the eye
• Colors on theme: Gold + blue

```html
<!DOCTYPE html>
<html lang="sv">
<head>
<meta charset="utf-8">
<title>Tallbergsgillet</title>
<link rel="stylesheet" href="https://fonts.googleapis.com/css2?family=EB+Garamond:wght@500;700&family=Gelasio&family=Montserrat:wght@700&family=Roboto:wght@400;500&display=swap">
<style>
:root{
  --navy:#13416c;
  --navy-dark:#173a66;
  --gold:#d6ac4f;
  --gold-soft:#e1bf6f;
  --ink:#3b3b3b;
  --muted:#8a8a8a;
  --panel:#f5f5f5;
  --white:#ffffff;
  --net-blue:#3b5a9a;
  --net-red:#dd4b39;
  --net-teal:#0e76a8;
  --net-sky:#1da1f2;
}
*{box-sizing:border-box;margin:0;padding:0}
html,body{width:1200px;height:2233px;overflow:hidden}
body{position:relative;background:var(--white);font-family:"Roboto",sans-serif;color:var(--ink)}
.abs{position:absolute}
.topbar{left:0;top:0;width:1200px;height:42px;background:var(--navy-dark)}
.follow{left:98px;top:9px;display:flex;gap:8px}
.dot{width:24px;height:24px;border-radius:50%;border:2px solid var(--white);display:inline-block}
.member-links{right:84px;top:6px;display:flex;gap:26px;color:var(--white);font-size:13px;align-items:center}
.member-links span{display:flex;align-items:center;gap:12px}
.member-links i{width:30px;height:30px;border-radius:50%;background:var(--gold);display:inline-block}
.nav{top:112px;font-size:13px;font-weight:500;color:var(--navy);letter-spacing:.3px}
.nav.active{color:var(--gold);border-top:2px solid var(--gold);border-bottom:2px solid var(--gold);padding:3px 2px}
.logo{left:517px;top:56px;width:168px;text-align:center;color:var(--gold);font-family:"EB Garamond",serif;font-weight:700;font-size:22px}
.logo i{display:block;width:34px;height:34px;border-radius:50%;background:var(--gold);margin:0 auto 6px}
.hero{left:0;top:180px;width:1200px;height:471px;background:linear-gradient(100deg,#cfe2ea 0%,#7fc3d4 22%,#9ed3de 45%,#b7dfe6 70%,#d6ebef 100%)}
.hero-arrow{top:347px;width:85px;height:85px;background:var(--white);display:flex;align-items:center;justify-content:center}
.featured{left:690px;top:302px;width:345px;height:191px;background:rgba(255,255,255,.28);border-right:4px solid var(--navy);text-align:right;padding:22px 30px 0 0;color:var(--white);font-family:"Gelasio",serif}
.featured h1{font-weight:400;font-size:60px;line-height:1}
.featured p{font-size:20px;margin-top:10px}
.btn{background:var(--navy);color:var(--white);font-size:12px;font-weight:500;display:inline-flex;align-items:center;justify-content:center;letter-spacing:.5px}
.featured .btn{width:112px;height:34px;margin-top:16px;font-family:"Roboto",sans-serif}
.heading{left:0;width:1200px;text-align:center;font-family:"EB Garamond",serif;font-weight:700;font-size:40px;color:var(--navy)}
.heading em{font-style:normal;color:var(--gold)}
.flourish{left:540px;width:120px;height:3px;background:var(--gold);border-radius:2px}
.offer{top:820px;width:301px}
.offer-img{height:169px;position:relative;background:linear-gradient(180deg,#263f7d 0%,#3a5aa0 45%,#1c2f5e 100%)}
.offer-img b{position:absolute;right:6px;bottom:6px;font-weight:400;font-size:38px;color:var(--gold)}
.offer-img b small{font-size:14px}
.offer-img.light b{color:var(--white)}
.offer h3{font-family:"Montserrat",sans-serif;font-size:18px;color:var(--gold);margin:14px 0 0 3px;letter-spacing:.5px}
.offer h4{font-size:13px;font-weight:500;color:var(--navy);margin:4px 0 0 3px}
.offer .meta{font-size:10px;color:var(--muted);margin:9px 0 0 3px;display:flex;gap:22px}
.offer p{font-size:12px;line-height:19px;color:var(--muted);margin:10px 0 0 3px}
.offer .row{display:flex;justify-content:space-between;align-items:center;margin-top:14px}
.share{display:flex;gap:9px;margin-left:2px}
.share i{width:29px;height:29px;border-radius:50%;background:#555;display:inline-block}
.share i:first-child{background:#aab2bb}
.offer .btn{width:112px;height:35px}
.blog{left:0;top:1278px;width:1200px;height:911px;background:var(--panel)}
.blog-meta{left:0;top:1402px;width:1200px;text-align:center;font-size:12px;color:#555}
.post{width:468px;height:257px;display:flex;background:var(--white)}
.post-img{width:215px;height:100%}
.post-body{position:relative;flex:1;padding:22px 20px 0 20px}
.tag{position:absolute;right:0;top:0;font-size:12px;color:var(--white);padding:2px 10px}
.tag.vendraly{background:var(--net-blue)}
.tag.glimtora{background:var(--gold)}
.who{display:flex;gap:8px;align-items:flex-start;font-size:10px}
.who i{width:32px;height:32px;border-radius:50%;background:var(--navy);border:2px solid var(--gold)}
.who b{color:#2277c9;font-weight:500}
.post p{font-size:12px;line-height:19px;color:var(--muted);margin-top:12px}
.dela{display:flex;align-items:center;gap:8px;margin-top:14px;font-size:11px;color:#555}
.dela i{width:26px;height:26px;border-radius:50%;display:inline-block}
.more{left:536px;top:2092px;width:128px;height:37px}
.footer{left:0;top:2189px;width:1200px;height:44px;background:var(--navy-dark);color:var(--white);font-size:12px;padding:13px 0 0 100px}
.footer .follow{left:943px;top:10px}
</style>
</head>
<body>
<div class="abs topbar"></div>
<div class="abs follow"><i class="dot" style="background:var(--net-blue)"></i><i class="dot" style="background:var(--net-teal)"></i><i class="dot" style="background:var(--net-sky)"></i><i class="dot" style="background:var(--net-red)"></i><i class="dot" style="background:var(--navy)"></i></div>
<div class="abs member-links"><span><i></i>Bli medlem</span><span><i></i>Medlemslogin</span></div>

<div class="abs nav active" style="left:100px;top:108px">HEM</div>
<div class="abs nav" style="left:204px">LIVSNJUTARRESOR</div>
<div class="abs nav" style="left:394px">INSPIRATION</div>
<div class="abs logo"><i></i>Tallbergsgillet</div>
<div class="abs nav" style="left:721px">MEDLEMSERBJUDANDEN</div>
<div class="abs nav" style="left:920px">OM ▾</div>
<div class="abs nav" style="left:1006px">KONTAKTA OSS</div>

<div class="abs hero" role="img" aria-label="Kvinna vilar i ett ljusblått geotermiskt bad omgivet av mörka lavaklippor"></div>
<div class="abs hero-arrow" style="left:13px"><svg width="14" height="24"><path d="M12 2 2 12l10 10" fill="none" stroke="#c9a24a" stroke-width="2"/></svg></div>
<div class="abs hero-arrow" style="left:1103px"><svg width="14" height="24"><path d="M2 2l10 10-10 10" fill="none" stroke="#c9a24a" stroke-width="2"/></svg></div>
<div class="abs featured"><h1>Featured</h1><p>liten beskrivning av post</p><span class="btn">LÄS MER</span></div>

<h2 class="abs heading" style="top:690px">Tallbergsgillets <em>Medlemserbjudnden</em></h2>
<div class="abs flourish" style="top:756px" role="img" aria-label="Guldornament"></div>

<div class="abs offer" style="left:98px">
  <div class="offer-img" role="img" aria-label="Kvällsvy över en upplyst hamnstad"><b>30%<small>Rabatt!</small></b></div>
  <h3>LJUSBRUNN SPA AB</h3><h4>Motionera Mera</h4>
  <div class="meta"><span>SEPTEMBER 3, 2016</span><span>REDAKTIONEN</span><span>0</span></div>
  <p>Lorem ipsum dolor sit amet, consectetuer adipiscing elit, sed diam nonummy nibh euismod tincidunt ut laoreet dolore magna aliquam erat volutpat. Ut wisi enim ad minim veniam</p>
  <div class="row"><div class="share"><i></i><i></i><i></i></div><span class="btn">LÄS MER</span></div>
</div>
<div class="abs offer" style="left:450px">
  <div class="offer-img light" role="img" aria-label="Kvällsvy över en upplyst hamnstad"><b>30%<small style="color:var(--white)"> Rabatt!</small></b></div>
  <h3>LJUSBRUNN SPA AB</h3><h4>Motionera Mera</h4>
  <div class="meta"><span>SEPTEMBER 3, 2016</span><span>REDAKTIONEN</span><span>0</span></div>
  <p>Lorem ipsum dolor sit amet, consectetuer adipiscing elit, sed diam nonummy nibh euismod tincidunt ut laoreet dolore magna aliquam erat volutpat. Ut wisi enim ad minim veniam</p>
  <div class="row"><div class="share"><i></i><i></i><i></i></div><span class="btn">LÄS MER</span></div>
</div>
<div class="abs offer" style="left:801px">
  <div class="offer-img" style="background:linear-gradient(180deg,#5a4f8f 0%,#3d5aa0 45%,#1c2f5e 100%)" role="img" aria-label="Skymning över en upplyst hamnstad"><b>30%<small>Rabatt!</small></b></div>
  <h3>LJUSBRUNN SPA AB</h3><h4>Motionera Mera</h4>
  <div class="meta"><span>SEPTEMBER 3, 2016</span><span>REDAKTIONEN</span><span>0</span></div>
  <p>Lorem ipsum dolor sit amet, consectetuer adipiscing elit, sed diam nonummy nibh euismod tincidunt ut laoreet dolore magna aliquam erat volutpat. Ut wisi enim ad minim veniam</p>
  <div class="row"><div class="share"><i></i><i></i><i></i></div><span class="btn">LÄS MER</span></div>
</div>

<div class="abs blog"></div>
<h2 class="abs heading" style="top:1308px">En trevlig rubrik <em>på ditt blogginlägg</em></h2>
<div class="abs flourish" style="top:1374px" role="img" aria-label="Guldornament"></div>
<div class="abs blog-meta">22 OKTOBER, 2016 | AV TALLBERGSGILLET | 0 KOMMENTARER | SPA, LIVSNJUTNING, YOGA</div>

<div class="abs post" style="left:98px;top:1456px">
  <div class="post-img" style="background:linear-gradient(160deg,#a07a5a,#d9cfc4 55%,#5a3a2e)" role="img" aria-label="Hotellrum med bäddad dubbelsäng"></div>
  <div class="post-body"><span class="tag vendraly">Vendraly</span>
    <div class="who"><i></i><div><b>Tallbergsgillet</b> &nbsp;23 oktober 19:21<br>5 &nbsp; 1 Kommentarer</div></div>
    <p>Lorem ipsum dolor amet, consectetuer adipiscing, dia nonummy nibh euismod tincidunt loreet dolore magna aliquam erat volutpat. wisi enim ad minim veniam, ntrud exerci tation ullamcorper rtis nisl ut aliquip commodo.</p>
    <div class="dela">Dela på <i style="background:var(--net-blue)"></i><i style="background:var(--net-red)"></i><i style="background:var(--net-teal)"></i><i style="background:var(--net-sky)"></i><i style="background:var(--navy)"></i></div>
  </div>
</div>
<div class="abs post" style="left:631px;top:1456px">
  <div class="post-img" style="background:linear-gradient(180deg,#8fa3b5,#c9cfc9 40%,#6b5a45)" role="img" aria-label="Två glas med citrondryck vid en hamn"></div>
  <div class="post-body"><span class="tag vendraly">Vendraly</span>
    <div class="who"><i></i><div><b>Tallbergsgillet</b> &nbsp;23 oktober 19:21<br>5 &nbsp; 1 Kommentarer</div></div>
    <p>Lorem ipsum dolor amet, consectetuer adipiscing, dia nonummy nibh euismod tincidunt loreet dolore magna aliquam erat volutpat. wisi enim ad minim veniam, ntrud exerci tation ullamcorper rtis nisl ut aliquip commodo.</p>
    <div class="dela">Dela på <i style="background:var(--net-blue)"></i><i style="background:var(--net-red)"></i><i style="background:var(--net-teal)"></i><i style="background:var(--net-sky)"></i><i style="background:var(--navy)"></i></div>
  </div>
</div>
<div class="abs post" style="left:98px;top:1767px">
  <div class="post-img" style="background:linear-gradient(180deg,#3c6fa6,#a8c3d6 45%,#e8dcae 75%,#f2f2f2)" role="img" aria-label="Två champagneglas mot blått hav"></div>
  <div class="post-body"><span class="tag glimtora">Glimtora</span>
    <div class="who"><i></i><div><b>Tallbergsgillet</b> &nbsp;23 oktober 19:21<br>5 &nbsp; 1 Kommentarer</div></div>
    <p>Lorem ipsum dolor amet, consectetuer adipiscing, dia nonummy nibh euismod tincidunt loreet dolore magna aliquam erat volutpat. wisi enim ad minim veniam, ntrud exerci tation ullamcorper rtis nisl ut aliquip commodo.</p>
    <div class="dela">Dela på <i style="background:var(--net-blue)"></i><i style="background:var(--net-red)"></i><i style="background:var(--net-teal)"></i><i style="background:var(--net-sky)"></i><i style="background:var(--navy)"></i></div>
  </div>
</div>
<div class="abs post" style="left:631px;top:1767px">
  <div class="post-img" style="background:linear-gradient(180deg,#d98bb0,#b07ab8 35%,#4a5a9a 65%,#1c2f5e)" role="img" aria-label="Hamnstad i rosa skymning"></div>
  <div class="post-body"><span class="tag glimtora">Glimtora</span>
    <div class="who"><i></i><div><b>Tallbergsgillet</b> &nbsp;23 oktober 19:21<br>5 &nbsp; 1 Kommentarer</div></div>
    <p>Lorem ipsum dolor amet, consectetuer adipiscing, dia nonummy nibh euismod tincidunt loreet dolore magna aliquam erat volutpat. wisi enim ad minim veniam, ntrud exerci tation ullamcorper rtis nisl ut aliquip commodo.</p>
    <div class="dela">Dela på <i style="background:var(--net-blue)"></i><i style="background:var(--net-red)"></i><i style="background:var(--net-teal)"></i><i style="background:var(--net-sky)"></i><i style="background:var(--navy)"></i></div>
  </div>
</div>

<span class="abs btn more">LÄS MER</span>

<div class="abs footer">Copyright 2016 NORRVIK STUDIO AB | All Right Reserved.
  <div class="abs follow"><i class="dot" style="background:var(--net-blue)"></i><i class="dot" style="background:var(--net-teal)"></i><i class="dot" style="background:var(--net-sky)"></i><i class="dot" style="background:var(--net-red)"></i><i class="dot" style="background:var(--navy)"></i></div>
</div>
</body>
</html>
```